13 Tavo - new website design project

Our company Tavo Electrical is developing a new lead generation website focused on Electrical, LED Lighting and Solar Power. We need a high converting website.

Example of our current website is www.tavoelectrical.com.au You can take content from this website for this new design. Our colours are red, black and white. For our new website we would like to promote Tavo, Bright Days Ahead. Please listen to the jingle.

The below link is the company jingle that we have developed.
http://www.tunecraftaudio.com.au/tav-tc-v1/

The key for this brief is to generate leads for Electrical, LED Lighting (for commercial) and Solar Power & Storage.

Target Market(s)

Business owners in Melbourne Victoria

Number of Pages Required

4 page

Colors
ec1f27
ffffff

Requirements
Must have
• This page must be clean, be in line with company branding and a high converting lead website.

```html
<!DOCTYPE html>
<html lang="en">
<head>
<meta charset="utf-8">
<title>Tavo Electrical</title>
<link rel="stylesheet" href="https://fonts.googleapis.com/css2?family=Titillium+Web:wght@400;600;700;900&family=Open+Sans:wght@400;600;700&display=swap">
<style>
:root{
  --red:#ec1f27;
  --red-deep:#c8161d;
  --ink:#2b2b2b;
  --dark:#333333;
  --dark-2:#444444;
  --footer:#2d2d2d;
  --footer-base:#3a3a3a;
  --light:#f4f4f4;
  --text:#555555;
  --white:#ffffff;
}
*{box-sizing:border-box;margin:0;padding:0}
html,body{width:1200px;height:3261px;overflow:hidden}
body{font-family:"Open Sans",Arial,sans-serif;color:var(--text);background:var(--white);position:relative}
.head-font{font-family:"Titillium Web",Arial,sans-serif}

/* header */
.topbar{height:115px;position:relative}
.brand{position:absolute;left:62px;top:22px;display:flex;align-items:center;gap:12px}
.brand-dot{width:46px;height:46px;border-radius:50%;background:var(--red)}
.brand-name{font-family:"Titillium Web",sans-serif;font-weight:900;font-size:44px;line-height:1;color:var(--red)}
.brand-tag{font-family:"Titillium Web",sans-serif;font-weight:700;font-size:15px;color:var(--ink);margin-top:2px}
.info{position:absolute;top:38px;display:flex;gap:10px;font-size:13px;line-height:18px;color:var(--ink)}
.info svg{flex:none;margin-top:2px}
.btn-view{position:absolute;left:991px;top:37px;width:150px;height:46px;background:var(--dark);color:var(--white);font-size:15px;display:flex;align-items:center;justify-content:center;gap:10px;font-weight:600}

.mainnav{height:46px;background:var(--red);display:flex;align-items:center;padding-left:59px;position:relative}
.mainnav a{color:var(--white);text-decoration:none;font-family:"Titillium Web",sans-serif;font-weight:700;font-size:16px;padding:0 22px;height:46px;display:flex;align-items:center}
.mainnav a.active{background:var(--dark);padding:0 14px;margin-right:12px}
.mainnav .nav-end{position:absolute;left:1094px;top:0;width:45px;height:46px;background:#111}

/* hero */
.hero{height:526px;position:relative;background:linear-gradient(100deg,#e9ebee 0%,#cfd3d8 45%,#8d949c 75%,#3d4550 100%)}
.hero-caption{position:absolute;left:59px;top:198px;width:532px;height:145px;background:rgba(30,30,30,.85);padding:28px 18px}
.hero-caption h1{font-family:"Titillium Web",sans-serif;font-weight:900;color:var(--white);font-size:44px;line-height:1;letter-spacing:1px}
.hero-caption p{color:var(--red);font-size:17px;line-height:22px;margin-top:10px}

/* why */
.why{height:661px;position:relative;text-align:center}
.section-title{font-family:"Titillium Web",sans-serif;font-weight:900;font-size:46px;color:var(--ink);letter-spacing:1px}
.section-title .accent{color:var(--red)}
.why .section-title{padding-top:70px}
.rule{width:166px;height:4px;background:var(--red);margin:8px auto 0}
.why-intro{width:940px;margin:36px auto 0;font-size:13.5px;line-height:23px;color:var(--text)}
.features{position:absolute;left:59px;top:291px;width:1080px;height:300px;display:flex}
.feature{flex:1;background:var(--dark);color:var(--white);text-align:center;padding-top:30px}
.feature:nth-child(even){background:var(--dark-2)}
.feature h3{font-family:"Titillium Web",sans-serif;font-weight:600;font-size:21px;margin-top:16px}
.feature p{font-size:12.5px;line-height:18px;width:200px;margin:10px auto 0}
.btn-red{display:inline-block;background:var(--red);color:var(--white);font-size:13px;font-weight:600;padding:9px 15px;margin-top:16px}

/* welcome */
.welcome{height:522px;background:var(--light);position:relative}
.welcome h2{position:absolute;left:59px;top:52px;font-family:"Titillium Web",sans-serif;font-weight:900;font-size:46px;color:var(--ink);letter-spacing:1px}
.welcome .lead{position:absolute;left:59px;top:110px;font-size:21px;color:var(--red)}
.welcome-media{position:absolute;left:11px;top:195px;width:619px;height:327px;background:linear-gradient(135deg,#d9c3b0 0%,#eceff2 40%,#b9c2cc 100%)}
.welcome-copy{position:absolute;left:641px;top:202px;width:500px;font-size:13.5px;line-height:28px;color:var(--text)}
.welcome-copy p+p{margin-top:26px}

/* services */
.services{height:756px;position:relative;background:radial-gradient(ellipse at 50% 30%,#d7262c 0%,var(--red-deep) 60%,#a81117 100%);text-align:center}
.services h2{padding-top:92px;font-family:"Titillium Web",sans-serif;font-weight:900;font-size:46px;color:var(--white);letter-spacing:1px;line-height:1}
.services .sub{color:var(--white);font-size:16px;margin-top:6px}
.service-card{position:absolute;top:234px;width:317px;height:418px;background:var(--white);padding:8px;text-align:left}
.service-img{height:184px;position:relative}
.service-label{position:absolute;left:0;right:0;bottom:0;height:40px;background:#3a3a3a;color:var(--white);font-size:16px;display:flex;align-items:center;justify-content:center}
.service-card h4{font-size:14.5px;color:var(--ink);text-align:center;font-weight:700;margin-top:14px}
.service-card p{font-size:12.5px;line-height:20px;margin:10px 9px 0;text-align:justify}
.service-card .simply{font-size:12.5px;font-weight:700;color:var(--ink);margin:10px 9px 0}
.service-card .more{position:absolute;right:18px;bottom:22px;font-size:13px;color:var(--ink)}

/* partners */
.partners{height:292px;position:relative}
.partner{position:absolute;top:96px;height:115px}

/* footer */
.footer{height:300px;background:var(--footer);position:relative;color:var(--white)}
.footer h5{font-family:"Titillium Web",sans-serif;font-weight:700;font-size:19px;position:absolute;top:30px}
.footer .col{position:absolute;top:82px;font-size:12.5px;line-height:22px}
.footer ul{list-style:none}
.footer ul li{line-height:33px;font-size:12.5px}
.contact-row{display:flex;gap:12px;margin-bottom:18px}
.contact-row .ico{width:24px;height:24px;border-radius:50%;background:var(--red);flex:none;display:flex;align-items:center;justify-content:center}
.field{width:288px;height:46px;border:1px solid #666;margin-top:24px;font-size:13px;padding:0 14px;display:flex;align-items:center}
.signup{width:288px;height:46px;background:var(--red);margin-top:16px;display:flex;align-items:center;justify-content:center;font-weight:700;font-size:13px}
.copyright{height:43px;background:var(--footer-base);color:#bbb;font-size:13px;display:flex;align-items:center;justify-content:center}
</style>
</head>
<body>

<header class="topbar">
  <div class="brand">
    <span class="brand-dot"></span>
    <div>
      <div class="brand-name">Tavo</div>
      <div class="brand-tag">Bright Days Ahead</div>
    </div>
  </div>
  <div class="info" style="left:374px">
    <svg width="20" height="24" viewBox="0 0 20 24"><path d="M10 0a9 9 0 0 0-9 9c0 7 9 15 9 15s9-8 9-15a9 9 0 0 0-9-9z" fill="#ec1f27"/><circle cx="10" cy="9" r="3.5" fill="#fff"/></svg>
    <div>8/44 Harlow St<br>Glen Iris VIC 3146</div>
  </div>
  <div class="info" style="left:583px">
    <svg width="22" height="22" viewBox="0 0 22 22"><circle cx="11" cy="11" r="9" fill="none" stroke="#ec1f27" stroke-width="3"/><path d="M11 6v5l4 3" stroke="#ec1f27" stroke-width="2.5" fill="none"/></svg>
    <div>07:30 - 19:00<br>Monday to Friday</div>
  </div>
  <div class="info" style="left:754px">
    <svg width="20" height="20" viewBox="0 0 20 20"><path d="M4 1l4 4-2 3c1 3 3 5 6 6l3-2 4 4-3 3C8 19 1 12 1 4z" fill="#ec1f27"/></svg>
    <div>139 270<br>service@tavoelectrical.com.au</div>
  </div>
  <div class="btn-view">Book a Viewing <span>&rsaquo;</span></div>
</header>

<nav class="mainnav">
  <a class="active">HOME</a>
  <a>TAVO STORY</a>
  <a>OUR WORK</a>
  <a>ELECTRICAL</a>
  <a>LED LIGHTING</a>
  <a>SOLAR POWER</a>
  <a>CONTACT US</a>
  <span class="nav-end"></span>
</nav>

<section class="hero" role="img" aria-label="Electrician in a hard hat holding plans beside a switchboard">
  <div class="hero-caption">
    <h1>SOLUTIONS PROVIDER</h1>
    <p>Australia's largest full integrated electrical &amp; energy solutions provider</p>
  </div>
</section>

<section class="why">
  <h2 class="section-title">WHY <span class="accent">CHOOSE</span> US?</h2>
  <div class="rule"></div>
  <p class="why-intro">Tavo Electrical was formed to be an expert Electricity Contracting Company providing services to all Residential and Commercial Customers.<br>With over 10 years of experience, Tavo Electrical has developed a highly-experienced team of professionals that ensure all<br>our customer expectations are met.</p>
  <div class="features">
    <div class="feature">
      <svg width="62" height="62" viewBox="0 0 62 62" fill="none" stroke="#fff" stroke-width="3"><rect x="6" y="8" width="50" height="34"/><path d="M14 18h10M14 26h10M34 18h14M34 26h14M14 34h34M20 50h22M31 42v8"/></svg>
      <h3>Professional Service</h3>
      <p>Creativity to create a better healthy and prosperous life for you and your owns.</p>
      <span class="btn-red">Read More</span>
    </div>
    <div class="feature">
      <svg width="62" height="62" viewBox="0 0 62 62" fill="none" stroke="#fff" stroke-width="4"><circle cx="29" cy="33" r="23"/><circle cx="29" cy="33" r="13"/><circle cx="29" cy="33" r="3" fill="#fff"/><path d="M29 33L52 10M46 8l6 2 2 6"/></svg>
      <h3>Workmanship guarantee</h3>
      <p>Creativity to create a better healthy and prosperous life for you and your owns.</p>
      <span class="btn-red">Read More</span>
    </div>
    <div class="feature">
      <svg width="62" height="62" viewBox="0 0 62 62" fill="none" stroke="#fff" stroke-width="3"><path d="M31 16a12 12 0 0 0-7 22v6h14v-6a12 12 0 0 0-7-22z"/><path d="M25 50h12M27 56h8M31 4v6M12 12l4 4M50 12l-4 4M6 30h6M50 30h6"/></svg>
      <h3>Fully insured</h3>
      <p>Creativity to create a better healthy and prosperous life for you and your owns.</p>
      <span class="btn-red">Read More</span>
    </div>
    <div class="feature">
      <svg width="62" height="62" viewBox="0 0 62 62" fill="none" stroke="#fff" stroke-width="3"><path d="M8 28c10-14 30-16 44-6l-4-8M52 22l-8 2"/><circle cx="22" cy="44" r="9"/><circle cx="42" cy="46" r="9"/></svg>
      <h3>Environmentally friendly</h3>
      <p>Creativity to create a better healthy and prosperous life for you and your owns.</p>
      <span class="btn-red">Read More</span>
    </div>
  </div>
</section>

<section class="welcome">
  <h2>WELCOME TO TAVO</h2>
  <p class="lead">Australia's largest full integrated electrical &amp; energy solutions provider.</p>
  <div class="welcome-media" role="img" aria-label="Hands holding a tablet playing a company video of a business meeting"></div>
  <div class="welcome-copy">
    <p>Tavo Electrical was formed to be an expert Electricity Contracting Company providing services to all Residential and Commercial Customers.With over 10 years of experience, Tavo Electrical has developed a highly-experienced team of professionals that ensure all our customer expectations are met.</p>
    <p>Tavo Electrical was formed to be an expert Electricity Contracting Company providing services to all Residential and Commercial Customers.With over 10 years of experience, Tavo Electrical has developed a highly-experienced team of professionals that ensure all our customer expectations are met.</p>
  </div>
</section>

<section class="services">
  <h2>WE PROVIDE SERVICES</h2>
  <p class="sub">Australia's largest full integrated electrical &amp; energy solutions provider.</p>

  <article class="service-card" style="left:61px">
    <div class="service-img" role="img" aria-label="Pliers cutting electrical wires" style="background:linear-gradient(135deg,#5a7fa8,#c9a27a 60%,#d33)">
      <div class="service-label">Electrical Services</div>
    </div>
    <h4>Creating Value Through Experience</h4>
    <p>At Halvane we focus primarily on real estate in New South Wales, Queensland and Victoria, but do transact in other states and sectors as required by clients or as opportunities present.</p>
    <p class="simply">Simply put, they are better homes!</p>
    <span class="more">Read More[+]</span>
  </article>

  <article class="service-card" style="left:443px">
    <div class="service-img" role="img" aria-label="Row of LED light bulbs" style="background:linear-gradient(180deg,#f2f2f2,#c9c9c9)">
      <div class="service-label">Led Lighting</div>
    </div>
    <h4>Benefit From In-Depth Market Expertise</h4>
    <p>Property assets generally present multiple opportunities. Astute negotiation for purchasing and creative strategy for redevelopment has earned us wide ranging successes</p>
    <p class="simply">Simply put, they are better homes!</p>
    <span class="more">Read More[+]</span>
  </article>

  <article class="service-card" style="left:822px">
    <div class="service-img" role="img" aria-label="Solar panels under a blue sky" style="background:linear-gradient(180deg,#4f8fd8 0%,#a9cdf0 45%,#2d4f7a 60%,#1d3252 100%)">
      <div class="service-label">Solar Power</div>
    </div>
    <h4>Partner With Professionals</h4>
    <p>Property assets generally present multiple opportunities. Astute negotiation for purchasing and creative strategy for redevelopment has earned us wide ranging successes</p>
    <p class="simply">Simply put, they are better homes!</p>
    <span class="more">Read More[+]</span>
  </article>
</section>

<section class="partners" aria-label="Partner brands">
  <div class="partner" style="left:65px;width:240px;background:#f2f2f2"></div>
  <div class="partner" style="left:374px;width:209px;background:#f4e500"></div>
  <div class="partner" style="left:652px;width:207px;background:#e5322d"></div>
  <div class="partner" style="left:933px;width:206px;background:#d6151c"></div>
</section>

<footer class="footer">
  <h5 style="left:61px">ABOUT US</h5>
  <div class="col" style="left:61px;width:270px">
    Tavo Electrical was formed to be an expert Electricity Contracting Company providing services to all Residential and Commercial Customers.<br>&nbsp;With over 10 years of experience, Tavo Electrical has developed a highly-experienced team of professionals that ensure all our customer expectations are met.
  </div>

  <h5 style="left:383px">NAVIGATION</h5>
  <ul class="col" style="left:383px;top:80px">
    <li>LED LIGHTING</li><li>SOLAR POWER</li><li>ELECTRICAL</li><li>CAREER</li><li>TERMS AND CONDITIONS</li><li>PRIVACY</li>
  </ul>

  <h5 style="left:572px">CONTACT DETAILS</h5>
  <div class="col" style="left:572px;width:240px">
    <div class="contact-row">
      <span class="ico"><svg width="10" height="13" viewBox="0 0 20 24"><path d="M10 0a9 9 0 0 0-9 9c0 7 9 15 9 15s9-8 9-15a9 9 0 0 0-9-9z" fill="#fff"/></svg></span>
      <div style="line-height:16px"><b>HEAD OFFICE</b><br>8/44 Harlow St<br>Glen Iris<br>VIC 3146</div>
    </div>
    <div class="contact-row">
      <span class="ico"><svg width="12" height="12" viewBox="0 0 20 20"><path d="M4 1l4 4-2 3c1 3 3 5 6 6l3-2 4 4-3 3C8 19 1 12 1 4z" fill="#fff"/></svg></span>
      <div>139 270</div>
    </div>
    <div class="contact-row">
      <span class="ico"><svg width="12" height="9" viewBox="0 0 12 9"><rect width="12" height="9" fill="#fff"/><path d="M0 0l6 5 6-5" stroke="#ec1f27" fill="none"/></svg></span>
      <div>service@tavoelectrical.com.au</div>
    </div>
  </div>

  <h5 style="left:850px">SUBSCRIBE NEWSLETTER</h5>
  <div class="col" style="left:850px;width:290px">
    Enter your email address for our mailing list to keep your self our latest updated.
    <div class="field">Email Address</div>
    <div class="signup">SIGN UP</div>
  </div>
</footer>
<div class="copyright">Copyright &copy; 2016 Tavo. All rights reserved</div>

</body>
</html>
```